Marrunga Gymkhana community event

We are looking for a bright new poster for our annual gymkhana event. We are a remote outback town in the Flinders Ranges, South Australia with a very small population (27 people)
Our picnic gymkhana is a community even bringing families amd their ponies from 100 of kms away for a fun filled day.
We have events for junior and senior riders events for spectators and generally lots of fun. Our poster should include our sponsor list, information like live evening entertainment, catering and bar facilities. The event is October 15th 2022.
I have photos etc if you need them will upload them as needed.
Poster should be easy to read and eye catching.

Target Market(s)

Local community

Industry/Entity Type

Horse and family event

Requirements
Must have
• Title sponsor list dates and general information
Nice to have
• Colours

```html
<!DOCTYPE html>
<html lang="en">
<head>
<meta charset="utf-8">
<title>2022 Marrunga Gymkhana</title>
<link rel="stylesheet" href="https://fonts.googleapis.com/css2?family=Graduate&family=Montserrat:wght@400;500;600;700&family=Oswald:wght@500&display=swap">
<style>
:root{
  --page:#ffffff;
  --dusk:#3a2a1c;
  --dusk-deep:#241a12;
  --gold:#d8b784;
  --sand:#d9bd86;
  --sand-light:#e6cf9f;
  --paper:#eceef1;
  --navy:#1c2a52;
  --brown:#5a2f1c;
  --bark:#4a2616;
  --red:#e33b3b;
  --tape:#f08a3c;
  --ink:#2b2b2b;
}
*{margin:0;padding:0;box-sizing:border-box}
html,body{width:1200px;height:2543px;overflow:hidden;background:var(--page)}
.stage{position:relative;width:1200px;height:2543px}
.poster{position:absolute;left:50px;top:513px;width:974px;height:1342px;transform:scale(1.1294);transform-origin:0 0;overflow:hidden;
  font-family:"Montserrat",sans-serif;background:var(--paper);box-shadow:0 10px 40px rgba(0,0,0,.35)}
.abs{position:absolute}
.hero-photo{left:0;top:0;width:974px;height:600px;background:radial-gradient(ellipse at 20% 45%,#5a4330 0%,transparent 45%),radial-gradient(ellipse at 85% 40%,#4d3a2a 0%,transparent 40%),linear-gradient(180deg,var(--dusk-deep) 0%,var(--dusk) 55%,#4e3a26 100%)}
.paper-band,.paper-foot{left:0;width:974px}
.year{top:72px;width:100%;text-align:center;font-weight:700;font-size:64px;letter-spacing:22px;color:var(--gold);padding-left:22px}
.title{width:100%;text-align:center;font-family:"Graduate",serif;font-size:128px;line-height:1;
  background:linear-gradient(180deg,#ffffff 20%,#a9a9a9 55%,#f4f4f4 80%);-webkit-background-clip:text;background-clip:text;color:transparent}
.title-1{top:142px}
.title-2{top:258px;font-size:120px;letter-spacing:2px}
.tagline{top:380px;width:100%;text-align:center;color:#fff;font-size:24px;line-height:28px;letter-spacing:.5px}
.date{top:440px;width:100%;text-align:center;color:var(--gold);font-weight:700;font-size:48px;letter-spacing:1px}
.date sup{font-size:26px;vertical-align:22px}
.snap{top:578px;width:260px;height:190px;border:6px solid #fff;background:linear-gradient(180deg,#c7c1b2 0%,#b48a5a 45%,#c08a55 100%)}
.tape{width:90px;height:28px;background:var(--tape);opacity:.85}
.info{left:66px;width:860px;color:var(--brown);font-weight:600;font-size:15.5px;white-space:nowrap}
.info b{font-size:22px}
.info-2{color:var(--navy);font-size:13.5px}
.info-2 b{font-size:22px;color:var(--brown)}
.pill{background:var(--navy);color:#fff;font-weight:600;font-size:17px;letter-spacing:.5px;text-align:center;border-radius:14px;height:26px;line-height:26px}
.noms{color:var(--brown);font-weight:600;font-size:15px;letter-spacing:.5px}
.fee{display:inline-flex;border-radius:10px;overflow:hidden;font-weight:700;font-size:15px;height:20px;line-height:20px}
.fee .k{background:var(--navy);color:#fff;padding:0 6px}
.fee .v{background:var(--red);color:#fff;padding:0 8px}
.small{color:var(--brown);font-size:11.5px;text-align:center;font-weight:500}
.spaced{letter-spacing:3px;color:#6d5a45}
.badge{border-radius:50%;background:var(--bark);border:5px solid #fff;color:var(--sand-light);font-weight:600;text-align:center;display:flex;align-items:center;justify-content:center;line-height:1.15}
.pin{width:16px;height:16px;border-radius:50%;background:var(--red);border:2px solid #fff}
.riders{left:640px;top:835px;width:320px;height:230px;background:linear-gradient(180deg,transparent 0%,rgba(120,70,40,.55) 35%,rgba(90,50,30,.75) 100%);border-radius:40% 40% 0 0}
.contact-head{left:66px;top:1060px;font-weight:700;font-size:23px;color:var(--bark)}
.contact-name{left:66px;top:1094px;font-family:"Oswald",sans-serif;font-size:34px;color:var(--red);letter-spacing:-.5px}
.contact-line{left:282px;font-weight:600;font-size:14px;color:var(--ink);display:flex;align-items:center;gap:8px}
.thanks{left:543px;top:1090px;font-size:10.5px;font-weight:600;color:var(--navy);line-height:13px}
.thanks small{display:block;font-size:9px;color:var(--ink);margin-top:3px}
.cause{left:66px;top:1152px;color:var(--ink);font-weight:600}
.cause p:first-child{font-size:14px}
.cause p{font-size:10.5px}
.social{left:732px;top:1160px;display:flex;align-items:center;gap:10px;color:#2c6fd0;font-size:24px}
.social i{display:block;width:22px;height:22px;background:#2c6fd0}
.sponsors{left:66px;top:1240px;font-size:17px;color:var(--ink)}
</style>
</head>
<body>
<div class="stage">
 <div class="poster">
  <div class="abs hero-photo" role="img" aria-label="Photo of young riders racing horses on a dusty outback track at dusk"></div>

  <svg class="abs paper-band" style="top:500px" width="974" height="620" viewBox="0 0 974 620" aria-hidden="true">
   <path d="M0 45 L40 38 L80 48 L130 35 L180 44 L240 30 L300 42 L360 28 L420 40 L480 26 L540 38 L600 25 L660 36 L720 22 L780 34 L840 24 L900 33 L974 20 L974 620 L0 620 Z" fill="#f4f4f4"/>
   <path d="M0 60 L50 52 L100 62 L160 48 L220 58 L290 44 L350 56 L420 42 L490 54 L560 40 L620 52 L690 38 L760 50 L830 36 L900 46 L974 34 L974 620 L0 620 Z" fill="var(--sand)"/>
   <path d="M0 60 L974 34 L974 620 L0 620 Z" fill="url(#stain)" opacity=".5"/>
   <defs><radialGradient id="stain" cx=".3" cy=".4" r=".7"><stop offset="0" stop-color="#f0dcae"/><stop offset="1" stop-color="#c9a56a"/></radialGradient></defs>
  </svg>

  <svg class="abs paper-foot" style="top:1030px" width="974" height="312" viewBox="0 0 974 312" aria-hidden="true">
   <path d="M0 30 L60 20 L120 34 L190 22 L250 36 L310 26 L360 40 L420 30 L480 44 L560 38 L640 50 L700 42 L760 54 L830 44 L900 52 L974 46 L974 312 L0 312 Z" fill="var(--paper)"/>
  </svg>

  <div class="abs year">2022</div>
  <div class="abs title title-1">MARRUNGA</div>
  <div class="abs title title-2">GYMKHANA</div>
  <div class="abs tagline">COME AND JOIN US AT ONE OF SOUTH AUSTRALIA`S<br>LONGEST RUNNING PICNIC RACES!</div>
  <div class="abs date">OCTOBER 15<sup>TH</sup> 2022</div>

  <div class="abs snap" style="left:75px" role="img" aria-label="Photo of a junior rider on a pony in a red dirt arena"></div>
  <div class="abs snap" style="left:358px" role="img" aria-label="Photo of a rider rounding a barrel at speed"></div>
  <div class="abs snap" style="left:641px" role="img" aria-label="Photo of three riders on horses in front of the ranges"></div>
  <div class="abs tape" style="left:140px;top:552px;transform:rotate(-6deg)"></div>
  <div class="abs tape" style="left:445px;top:552px;transform:rotate(5deg)"></div>
  <div class="abs tape" style="left:718px;top:550px;transform:rotate(-4deg)"></div>

  <div class="abs info" style="top:776px">ADMISSION FEES <b>$15</b> CAOREN U/S REE : FOOD &amp; BAR FACILITIES ALL DAY : ROAST &amp; RIBS DINNER</div>
  <div class="abs info info-2" style="top:801px">ALL LED EVENTS (UA) WILL GE RUN FIRST FROM &nbsp;<b>9:30 AM</b>&nbsp; MAIN PROGRAM TO COMMENCE &nbsp;<b>10:30 AM</b></div>

  <div class="abs pill" style="left:120px;top:846px;width:198px">HORSE EVENTS</div>
  <div class="abs noms" style="left:68px;top:884px">GYMKHANA EVENT NOMINATIONS :</div>
  <div class="abs" style="left:72px;top:910px;display:flex;gap:14px">
   <span class="fee"><span class="k">Junior</span><span class="v">$20.00</span></span>
   <span class="fee"><span class="k">Senior</span><span class="v">$30.00</span></span>
  </div>
  <div class="abs small spaced" style="left:66px;top:934px;width:300px">FOR THE DAY (PER HOUR)</div>
  <div class="abs small" style="left:66px;top:951px;width:300px">Junior age group : Led, approx,<br>8 and under, 14 and under, not led</div>

  <div class="abs pill" style="left:418px;top:846px;width:242px">NON-HORSE EVENTS</div>
  <div class="abs" style="left:425px;top:886px"><span class="fee" style="font-size:15px"><span class="k" style="padding:0 10px">All nominations</span><span class="v">$2.00</span></span></div>
  <div class="abs small" style="left:440px;top:913px;width:186px;font-weight:600">per person per event</div>

  <div class="abs badge" style="left:342px;top:938px;width:146px;height:146px;font-size:19px">Stalls &amp;<br>Outback<br>Childcare</div>
  <div class="abs pin" style="left:414px;top:934px"></div>
  <div class="abs badge" style="left:492px;top:940px;width:128px;height:128px;font-size:18px">ROAST<br>&amp; RIBS<br>DINNER</div>
  <div class="abs pin" style="left:556px;top:936px"></div>

  <div class="abs riders" role="img" aria-label="Photo of young riders in helmets on horses"></div>

  <div class="abs contact-head">For more info contact</div>
  <div class="abs contact-name">JODIE PENNACK</div>
  <div class="abs contact-line" style="top:1104px">
   <svg width="14" height="14" viewBox="0 0 24 24" aria-hidden="true"><path d="M6.6 10.8a15 15 0 0 0 6.6 6.6l2.2-2.2a1 1 0 0 1 1-.25 11.4 11.4 0 0 0 3.6.57 1 1 0 0 1 1 1V20a1 1 0 0 1-1 1A17 17 0 0 1 3 4a1 1 0 0 1 1-1h3.5a1 1 0 0 1 1 1c0 1.25.2 2.45.57 3.57a1 1 0 0 1-.25 1z" fill="var(--red)"/></svg>8651 2270</div>
  <div class="abs contact-line" style="top:1124px">
   <svg width="14" height="12" viewBox="0 0 24 20" aria-hidden="true"><rect x="1" y="1" width="22" height="18" fill="var(--red)"/><path d="M1 1l11 9 11-9" stroke="#fff" stroke-width="2" fill="none"/></svg>jodiepennack@mailbox.com</div>

  <div class="abs thanks">THE GYMKHANA COMMITTEE WISHES TO THANK ALL<br>SPONSORS AND DONORS FOR THEIR GENEROUS SUPPORT`<small>All riders ride at their own risk. Dogs must be on leads al all times.</small></div>

  <div class="abs cause">
   <p>HELP-SUPPORT THE CAUSE : NO BYO ALCOHOL</p>
   <p>PROCEEDS TO OUTBACK AIR MEDICAL SERVICE &amp; MARRUNGA PROGRESS ASSOCIATION :</p>
   <p>Please be advised thiss non-SARA affiliated event for nun registered horses, riders, owners, trainers.</p>
  </div>

  <div class="abs social"><i></i>Townbook</div>

  <div class="abs sponsors">OUR SPONCERS:</div>
 </div>
</div>
</body>
</html>
```